Professionelles Social Media Material für Reinigungsdienstleister
Zielgruppe
Wir reinigen Privathaushalte, Ferienwohnungen, Arztpraxen und Büroräume.
Aufgabenstellung
Ich wünsche Material für ein professionelles Auftreten bei Facebook und Instagram. Wir müssen bei Facebook leider neu starten und haben Instagram bei dieser Firma bisher vernachlässigt.
Nun wollen wir unser Social Media professionell erscheinen lassen und einen Plan für die kommenden 2 Monate erstellen. Wir suchen dafür mindestens 20 passende Postings und die Inhalte für den Start.
Nachtrag zu den Postings: Wir wollen ganz allgemeinen Content und sind offen für alle Vorschläge. Es kann gern auch eine Sommeraktion beworben werden, bei der wir Neukunden 100€ schenken und eine Aktion, bei der es eine kostenlose Erstreinigung gibt um unsere Leistung zu testen.

```html
<!DOCTYPE html>
<html lang="de">
<head>
<meta charset="utf-8">
<title>Wohnglanz Pilot – Social Media Postings</title>
<link href="https://fonts.googleapis.com/css2?family=Montserrat:ital,wght@0,400;0,500;0,600;0,700;0,800;1,500;1,600;1,700;1,800&display=swap" rel="stylesheet">
<style>
:root{
  --canvas:#e3e3e3;
  --paper:#ffffff;
  --blue:#6fa3cb;
  --blue-mid:#5b93c2;
  --blue-deep:#2f78b6;
  --blue-soft:#c6dbec;
  --blue-pale:#e4eef7;
  --yellow:#f6e76c;
  --navy:#2b4766;
  --white:#ffffff;
}
*{box-sizing:border-box;margin:0;padding:0}
html,body{width:1200px;height:2286px;overflow:hidden;background:var(--canvas)}
body{font-family:"Montserrat",Arial,sans-serif;color:var(--navy)}
.board{display:grid;grid-template-columns:repeat(3,314px);grid-auto-rows:395px;column-gap:55px;row-gap:50px;padding:54px 0 0 74px}
.poster{position:relative;width:314px;height:395px;background:var(--paper);overflow:hidden;box-shadow:0 2px 5px rgba(0,0,0,.18)}
.shapes{position:absolute;left:0;top:0;width:314px;height:395px}
.a{position:absolute}
.brand{position:absolute;left:9px;top:16px;display:flex;align-items:center;gap:4px}
.brand-mark{width:10px;height:10px;background:var(--navy)}
.brand-name{font-size:8px;font-weight:800;line-height:1.05;color:var(--navy)}
.title{position:absolute;left:112px;top:22px;font-size:24.5px;font-weight:800;line-height:.98;color:var(--white);letter-spacing:.2px}
.pill{position:absolute;background:var(--yellow);border-radius:50%;transform:rotate(-4deg)}
.pill-text{position:absolute;font-style:italic;font-weight:800;color:var(--blue-deep);line-height:1.05}
.photo{position:absolute;overflow:hidden}
.foot{position:absolute;color:var(--white);font-size:10.5px;font-weight:600;line-height:1.35}
.foot.it{font-style:italic;font-weight:500}
.side{position:absolute;color:var(--blue-deep);font-style:italic;font-weight:600;font-size:10.5px;line-height:1.3;z-index:2}
.body-text{position:absolute;color:var(--blue-deep);font-size:10.5px;line-height:1.35;font-weight:500}
.body-text b{font-weight:700}
.quote{position:absolute;font-size:54px;font-weight:800;color:var(--blue-mid);font-style:italic;line-height:1;letter-spacing:-4px}
.label{position:absolute;font-size:7.5px;color:var(--blue-deep);font-weight:500}
.list{list-style:none}
.list li{display:flex;gap:6px;align-items:flex-start;margin-bottom:6px}
.ring{flex:none;width:6px;height:6px;border-radius:50%;border:1px solid var(--blue-deep);margin-top:4px}
</style>
</head>
<body>
<svg width="0" height="0" style="position:absolute">
  <defs>
    <symbol id="spark" viewBox="0 0 20 20"><path d="M10 0 C11 7 13 9 20 10 C13 11 11 13 10 20 C9 13 7 11 0 10 C7 9 9 7 10 0Z"/></symbol>
    <symbol id="header" viewBox="0 0 314 395"><path d="M82,0 H314 V100 C270,103 200,110 150,107 C108,104 84,82 80,52 Z"/></symbol>
  </defs>
</svg>

<main class="board">

<!-- 1 Helden -->
<section class="poster">
  <svg class="shapes" viewBox="0 0 314 395">
    <use href="#header" fill="var(--blue)"/>
    <path d="M0,285 C70,275 150,300 220,288 C270,280 300,272 314,268 V395 H0Z" fill="var(--blue)"/>
    <path d="M80,248 C140,236 230,232 314,250 V280 C250,300 150,292 70,278Z" fill="var(--blue-soft)"/>
  </svg>
  <div class="brand"><span class="brand-mark"></span><span class="brand-name">Wohnglanz<br>Pilot</span></div>
  <div class="title">REINIGUNGS<br>SERVICE</div>
  <div class="photo" role="img" aria-label="Frau im Heldinnenkostüm mit rotem Handschuh und buntem Staubwedel" style="left:95px;top:165px;width:200px;height:120px;border-radius:48% 52% 40% 50%/55% 45% 50% 45%;background:linear-gradient(120deg,#c4314a 0%,#e3b7a2 45%,#f3c94e 70%,#e36fa6 100%)"></div>
  <div class="pill" style="left:60px;top:105px;width:250px;height:60px"></div>
  <div class="pill-text" style="left:110px;top:120px;font-size:15px">Sauberkeit ist unsere<br>Leidenschaft</div>
  <div class="side" style="left:18px;top:172px;transform:rotate(-16deg);font-weight:500;font-size:10px">Jetzt<br>Angebot<br>einholen!</div>
  <div class="foot" style="left:58px;top:326px">Das bisschen<br>Haushalt macht sich von allein …<br>Du brauchst nur den <b><i>richtigen Helden!</i></b></div>
</section>

<!-- 2 Team -->
<section class="poster">
  <svg class="shapes" viewBox="0 0 314 395">
    <use href="#header" fill="var(--blue)"/>
    <path d="M0,300 C80,285 150,300 220,290 C270,283 300,270 314,262 V395 H0Z" fill="var(--blue)"/>
    <path d="M60,260 C150,240 250,240 314,250 V280 C230,300 140,300 60,285Z" fill="var(--blue-soft)"/>
    <use href="#spark" x="30" y="330" width="18" height="18" fill="var(--blue-soft)"/>
    <circle cx="22" cy="320" r="3" fill="var(--blue-soft)"/>
  </svg>
  <div class="brand"><span class="brand-mark"></span><span class="brand-name">Wohnglanz<br>Pilot</span></div>
  <div class="title">REINIGUNGS<br>SERVICE</div>
  <div class="photo" role="img" aria-label="Drei Reinigungskräfte in blauen Schürzen mit Staubsauger und Putzeimer" style="left:115px;top:65px;width:180px;height:235px;border-radius:40px 40px 10px 10px;background:linear-gradient(180deg,#c9d9e6 0%,#3f86c4 45%,#2f6fa8 70%,#e8d23a 100%)"></div>
  <div class="side" style="left:27px;top:188px;font-weight:500">Zuverlässig,<br>pünktlich und<br>blitzsauber</div>
  <div class="foot it" style="left:62px;top:330px">Wir sorgen für glanzvolle Ergebnisse<br>in privaten <b>Haushalten, Büros</b><br><b>und Gewerbe.</b></div>
</section>

<!-- 3 Sommeraktion -->
<section class="poster">
  <svg class="shapes" viewBox="0 0 314 395">
    <use href="#header" fill="var(--blue)"/>
    <path d="M0,262 C90,250 200,270 314,255 V395 H0Z" fill="var(--blue)"/>
    <use href="#spark" x="30" y="328" width="18" height="18" fill="var(--blue-soft)"/>
    <circle cx="24" cy="320" r="3" fill="var(--blue-soft)"/>
  </svg>
  <div class="brand"><span class="brand-mark"></span><span class="brand-name">Wohnglanz<br>Pilot</span></div>
  <div class="title">REINIGUNGS<br>SERVICE</div>
  <div class="pill" style="left:55px;top:100px;width:250px;height:55px"></div>
  <div class="pill-text" style="left:110px;top:118px;font-size:17px">Sommeraktion!</div>
  <div class="photo" role="img" aria-label="Überraschte Frau am sonnigen Strand unter blauem Himmel" style="left:15px;top:155px;width:285px;height:158px;border-radius:50% 48% 45% 50%/55% 50% 50% 45%;border:3px solid var(--white);background:linear-gradient(100deg,#8fbfe3 0%,#d8a58a 35%,#cfe4f3 60%,#e9dcc0 100%)"></div>
  <div class="a" style="left:155px;top:172px;transform:rotate(-15deg);color:var(--blue-deep);font-weight:800;font-style:italic;line-height:1.05">
    <div style="font-size:9px">Jeder<br>Neukunde<br>bekommt:</div>
    <div style="font-size:15px;margin-top:6px;margin-left:10px">€ 100,-</div>
    <div style="font-size:15px;margin-left:10px">GESCHENKT!</div>
  </div>
  <div class="foot it" style="left:58px;top:336px">Damit du entspannt in den Urlaub<br>fahren kannst!</div>
</section>

<!-- 4 Checkliste -->
<section class="poster">
  <svg class="shapes" viewBox="0 0 314 395">
    <use href="#header" fill="var(--blue)"/>
    <path d="M0,355 C100,348 210,355 314,348 V395 H0Z" fill="var(--blue)"/>
    <ellipse cx="100" cy="215" rx="95" ry="62" fill="var(--blue)"/>
    <ellipse cx="50" cy="146" rx="30" ry="22" fill="none" stroke="var(--blue-soft)" stroke-width="1.5"/>
    <use href="#spark" x="30" y="218" width="16" height="16" fill="var(--blue-soft)"/>
    <g stroke="var(--blue-deep)" stroke-width="1.5" fill="none">
      <line x1="190" y1="202" x2="215" y2="194"/>
      <line x1="175" y1="260" x2="200" y2="270"/>
      <line x1="185" y1="240" x2="205" y2="235"/>
      <rect x="224" y="182" width="24" height="5" rx="2.5"/><rect x="224" y="190" width="24" height="5" rx="2.5"/><rect x="224" y="198" width="24" height="5" rx="2.5"/><rect x="224" y="206" width="24" height="5" rx="2.5"/>
      <rect x="224" y="240" width="20" height="40" /><line x1="234" y1="240" x2="234" y2="280"/>
      <rect x="45" y="305" width="12" height="34" rx="3"/><line x1="57" y1="314" x2="74" y2="314"/>
      <rect x="165" y="322" width="14" height="18" rx="2"/><rect x="169" y="326" width="6" height="10" rx="1"/>
    </g>
  </svg>
  <div class="brand"><span class="brand-mark"></span><span class="brand-name">Wohnglanz<br>Pilot</span></div>
  <div class="title">REINIGUNGS<br>SERVICE</div>
  <div class="pill" style="left:60px;top:105px;width:250px;height:70px"></div>
  <div class="pill-text" style="left:110px;top:123px;font-size:15.5px">Checkliste:<br>&nbsp;&nbsp;&nbsp;Frühjahrsputz</div>
  <div class="a" style="left:64px;top:180px;color:var(--white);font-size:10px;line-height:1.2;font-weight:500">Dinge, die beim<br>Frühjahrsputz<br>oft vergessen<br>werden …<br><span style="font-size:12px;display:block;margin-top:6px;line-height:1.15">Wir vergessen<br>nichts!</span></div>
  <div class="label" style="left:222px;top:220px">Heizkörper</div>
  <div class="label" style="left:222px;top:286px">Fensterrahmen</div>
  <div class="label" style="left:78px;top:318px">Türgriffe</div>
  <div class="label" style="left:185px;top:318px">Lichtschalter</div>
  <div class="foot it" style="left:56px;top:367px">Jetzt Angebot einholen!</div>
</section>

<!-- 5 Fenster -->
<section class="poster">
  <svg class="shapes" viewBox="0 0 314 395">
    <use href="#header" fill="var(--blue)"/>
    <path d="M0,278 C90,268 200,292 314,270 V395 H0Z" fill="var(--blue)"/>
    <use href="#spark" x="30" y="325" width="18" height="18" fill="var(--blue-soft)"/>
    <circle cx="24" cy="318" r="3" fill="var(--blue-soft)"/>
  </svg>
  <div class="brand"><span class="brand-mark"></span><span class="brand-name">Wohnglanz<br>Pilot</span></div>
  <div class="title">REINIGUNGS<br>SERVICE</div>
  <div class="pill" style="left:60px;top:105px;width:245px;height:65px"></div>
  <div class="pill-text" style="left:133px;top:117px;font-size:14.5px">Glas- und<br>Fensterreinigung</div>
  <div class="photo" role="img" aria-label="Mann reinigt eine große Glasscheibe mit einem Fensterwischer" style="left:14px;top:170px;width:290px;height:138px;border-radius:48% 50% 45% 48%/50% 55% 45% 50%;border:3px solid var(--white);background:linear-gradient(110deg,#d7e8f5 0%,#9cc6e6 45%,#7aa7c9 70%,#2a2c33 100%)"></div>
  <div class="a" style="left:12px;top:160px;background:var(--blue);color:var(--white);padding:3px 10px 4px;border-radius:3px;transform:rotate(-10deg);font-size:12px;font-weight:600;line-height:1">garantiert<br><span style="font-size:8px;font-style:italic">streifenfrei</span></div>
  <div class="foot" style="left:72px;top:340px">Wir bringen Ihre Fenster<br>zum Strahlen!</div>
</section>

<!-- 6 Kundenstimmen -->
<section class="poster">
  <svg class="shapes" viewBox="0 0 314 395">
    <use href="#header" fill="var(--blue)"/>
    <path d="M110,372 C90,355 82,320 86,290 C95,215 160,185 240,188 C300,190 330,215 340,230 V352 C300,372 230,378 170,365 C140,385 100,392 75,388 C92,382 104,378 110,372Z" fill="var(--white)" stroke="var(--blue-soft)" stroke-width="3"/>
    <ellipse cx="35" cy="140" rx="28" ry="22" fill="none" stroke="var(--blue-pale)" stroke-width="1.5"/>
  </svg>
  <div class="brand"><span class="brand-mark"></span><span class="brand-name">Wohnglanz<br>Pilot</span></div>
  <div class="title">REINIGUNGS<br>SERVICE</div>
  <div class="pill" style="left:60px;top:105px;width:250px;height:65px"></div>
  <div class="pill-text" style="left:110px;top:134px;font-size:14.5px">was Kunden sagen:</div>
  <div class="quote" style="left:38px;top:180px">”</div>
  <div class="body-text" style="left:111px;top:215px;font-size:10.3px;line-height:1.38"><b><i>„Zuverlässig, pünktlich<br>und blitzsauber</i></b> –<br>ich empfehle euch gerne<br>weiter!“ – Sabine Krüger<br>Wir sagen:<br>Danke für das Vertrauen!</div>
</section>

<!-- 7 Erstreinigung -->
<section class="poster">
  <svg class="shapes" viewBox="0 0 314 395">
    <use href="#header" fill="var(--blue)"/>
    <path d="M0,262 C90,252 200,272 314,250 V395 H0Z" fill="var(--blue)"/>
    <use href="#spark" x="22" y="332" width="18" height="18" fill="var(--blue-soft)"/>
    <circle cx="16" cy="326" r="3" fill="var(--blue-soft)"/>
  </svg>
  <div class="brand"><span class="brand-mark"></span><span class="brand-name">Wohnglanz<br>Pilot</span></div>
  <div class="title">REINIGUNGS<br>SERVICE</div>
  <div class="pill" style="left:60px;top:105px;width:250px;height:65px"></div>
  <div class="pill-text" style="left:110px;top:120px;font-size:11px;font-style:normal;font-weight:500">Wir <b style="font-weight:800">schenken</b> dir<br>die Erstreinigung</div>
  <div class="photo" role="img" aria-label="Lachende Frau mit Locken und pinken Putzhandschuhen vor türkisem Hintergrund" style="left:15px;top:168px;width:285px;height:145px;border-radius:48% 50% 45% 48%/52% 50% 48% 50%;border:3px solid var(--white);background:linear-gradient(100deg,#5ea9ab 0%,#6fb5b4 50%,#e9b24c 75%,#d94e8d 100%)"></div>
  <div class="a" style="left:45px;top:235px;color:var(--white);font-size:19px;font-weight:800;font-style:italic">TESTE UNS!</div>
  <div class="foot" style="left:82px;top:340px;font-weight:500">Erstreinigung gratis · <b>Jetzt</b><br><b>Angebot einholen!</b></div>
</section>

<!-- 8 Stellenanzeige -->
<section class="poster">
  <svg class="shapes" viewBox="0 0 314 395">
    <use href="#header" fill="var(--blue)"/>
    <path d="M90,355 C75,330 70,300 75,270 C88,205 160,180 240,182 C300,185 330,210 340,225 V340 C300,365 230,368 170,355 C140,370 100,375 70,372 C82,368 88,362 90,355Z" fill="var(--white)" stroke="var(--blue-soft)" stroke-width="3"/>
    <circle cx="28" cy="412" r="20" fill="var(--blue)"/>
    <circle cx="135" cy="412" r="20" fill="var(--blue)"/>
    <circle cx="90" cy="380" r="4" fill="var(--blue)"/>
    <circle cx="42" cy="358" r="6" fill="none" stroke="var(--blue)" stroke-width="1.2"/>
    <circle cx="192" cy="380" r="6" fill="none" stroke="var(--blue)" stroke-width="1.2"/>
  </svg>
  <div class="brand"><span class="brand-mark"></span><span class="brand-name">Wohnglanz<br>Pilot</span></div>
  <div class="title">REINIGUNGS<br>SERVICE</div>
  <div class="pill" style="left:60px;top:105px;width:250px;height:60px"></div>
  <div class="pill-text" style="left:111px;top:126px;font-size:14.5px">WIR STELLEN EIN!</div>
  <div class="quote" style="left:35px;top:175px">”</div>
  <div class="body-text" style="left:111px;top:205px;font-size:10.3px;line-height:1.38;color:var(--blue-mid)"><span style="color:var(--blue-deep);font-weight:600">Wir suchen Verstärkung!</span><br>(m/w/d) <b style="color:var(--blue-deep)">in Teilzeit<br>gesucht – fair bezahlt,<br>familiäres Team.</b><br>Sende uns deine<br>Bewerbung per Mail<br>oder ruf an!</div>
</section>

<!-- 9 Büroreinigung -->
<section class="poster">
  <svg class="shapes" viewBox="0 0 314 395">
    <use href="#header" fill="var(--blue)"/>
    <path d="M0,268 C90,255 200,278 314,256 V395 H0Z" fill="var(--blue)"/>
    <use href="#spark" x="28" y="335" width="18" height="18" fill="var(--blue-soft)"/>
    <circle cx="22" cy="327" r="3" fill="var(--blue-soft)"/>
  </svg>
  <div class="brand"><span class="brand-mark"></span><span class="brand-name">Wohnglanz<br>Pilot</span></div>
  <div class="title">REINIGUNGS<br>SERVICE</div>
  <div class="pill" style="left:60px;top:105px;width:250px;height:60px"></div>
  <div class="pill-text" style="left:158px;top:116px;font-size:14.5px;font-style:normal">Büroreinigung</div>
  <div class="pill-text" style="left:158px;top:134px;font-size:8px">warum sie so wichtig ist</div>
  <div class="photo" role="img" aria-label="Frau streckt sich zufrieden an ihrem aufgeräumten Büroarbeitsplatz" style="left:15px;top:158px;width:288px;height:148px;border-radius:48% 50% 45% 48%/52% 50% 48% 50%;border:3px solid var(--white);background:linear-gradient(100deg,#e9eef3 0%,#b9cddc 40%,#c5714a 60%,#dfe6ec 100%)"></div>
  <div class="a" style="left:198px;top:195px;width:105px;height:105px;border-radius:50%;background:var(--blue);color:var(--white);font-size:6px;text-align:center;padding:33px 8px 0;line-height:1.35">Wussten Sie, dass<br><b>saubere Arbeitsplätze</b><br>die <b>Produktivität</b> um<br>12 % steigern können?</div>
  <div class="foot" style="left:84px;top:325px">Jetzt Reinigungsplan für Ihr<br>Büro erstellen lassen.</div>
</section>

<!-- 10 Spezialreinigung -->
<section class="poster">
  <svg class="shapes" viewBox="0 0 314 395">
    <use href="#header" fill="var(--blue)"/>
    <path d="M0,325 C90,318 200,330 314,318 V395 H0Z" fill="var(--blue)"/>
    <use href="#spark" x="24" y="348" width="18" height="18" fill="var(--blue-soft)"/>
    <use href="#spark" x="265" y="345" width="20" height="20" fill="var(--blue-soft)"/>
    <circle cx="18" cy="340" r="3" fill="var(--blue-soft)"/>
    <circle cx="258" cy="372" r="3" fill="var(--blue-soft)"/>
  </svg>
  <div class="brand"><span class="brand-mark"></span><span class="brand-name">Wohnglanz<br>Pilot</span></div>
  <div class="title">REINIGUNGS<br>SERVICE</div>
  <div class="pill" style="left:60px;top:105px;width:250px;height:60px"></div>
  <div class="pill-text" style="left:110px;top:128px;font-size:15px">Spezialreinigung</div>
  <div class="photo" role="img" aria-label="Gelbe Quietscheente auf einem sauberen Badewannenrand vor türkisen Fliesen" style="left:15px;top:160px;width:288px;height:142px;border-radius:48% 50% 45% 48%/52% 50% 48% 50%;background:linear-gradient(180deg,#2f86a6 0%,#5aa9c2 55%,#eef3f5 75%,#e6d23c 100%)"></div>
  <div class="a" style="left:100px;top:187px;color:var(--white);font-size:12px;font-weight:700;text-align:center;line-height:1.2">Schimmel in<br>der Dusche?</div>
  <div class="a" style="left:15px;top:238px;width:128px;height:62px;border-radius:50%;background:var(--blue-pale);border:2px solid var(--white)"></div>
  <div class="a" style="left:28px;top:248px;transform:rotate(-8deg);font-size:7px;line-height:1.3;color:var(--blue-deep)"><b>Kein Problem.</b> Wir über-<br>nehmen auch schwierige<br>Fälle – professionell und<br>hygienisch.“</div>
  <div class="foot" style="left:64px;top:354px;font-size:11px">Jetzt Angebot einholen!</div>
</section>

<!-- 11 Umzug -->
<section class="poster">
  <svg class="shapes" viewBox="0 0 314 395">
    <use href="#header" fill="var(--blue)"/>
    <path d="M0,290 C90,282 200,305 314,290 V395 H0Z" fill="var(--blue)"/>
    <path d="M60,245 C150,235 250,240 314,250 V290 C230,300 140,300 60,285Z" fill="var(--blue-soft)"/>
    <use href="#spark" x="10" y="270" width="18" height="18" fill="var(--blue-soft)"/>
  </svg>
  <div class="brand"><span class="brand-mark"></span><span class="brand-name">Wohnglanz<br>Pilot</span></div>
  <div class="title">REINIGUNGS<br>SERVICE</div>
  <div class="pill" style="left:60px;top:105px;width:250px;height:65px"></div>
  <div class="pill-text" style="left:110px;top:116px;font-size:14.5px;font-style:normal">Umzugsreinigung,<br>Endreinigung</div>
  <div class="side" style="left:34px;top:195px;font-size:9px;font-style:normal;font-weight:500">Neuer Mieter,<br>neuer Glanz!</div>
  <div class="photo" role="img" aria-label="Gestapelte Umzugskartons mit Besen, Kehrschaufel und Teppichrolle" style="left:120px;top:165px;width:150px;height:125px;border-radius:10px;background:linear-gradient(160deg,#f1e6d8 0%,#d9b48c 45%,#c89a6e 75%,#f2f2f2 100%)"></div>
  <div class="foot" style="left:60px;top:335px;font-size:7px;font-weight:500">Wir übernehmen die Endreinigung beim Umzug –<br>zuverlässig und gründlich.</div>
  <div class="foot" style="left:60px;top:356px;font-size:11px">Jetzt Angebot einholen!</div>
</section>

<!-- 12 Umfrage -->
<section class="poster">
  <svg class="shapes" viewBox="0 0 314 395">
    <use href="#header" fill="var(--blue)"/>
    <path d="M100,365 C80,345 75,315 78,285 C88,215 160,190 240,192 C300,195 330,220 340,235 V350 C300,370 230,375 170,362 C140,380 100,386 72,383 C88,376 98,372 100,365Z" fill="var(--white)" stroke="var(--blue-soft)" stroke-width="3"/>
  </svg>
  <div class="brand"><span class="brand-mark"></span><span class="brand-name">Wohnglanz<br>Pilot</span></div>
  <div class="title">REINIGUNGS<br>SERVICE</div>
  <div class="pill" style="left:60px;top:105px;width:250px;height:60px"></div>
  <div class="pill-text" style="left:110px;top:123px;font-size:17px">Umfrage</div>
  <div class="quote" style="left:38px;top:175px">”</div>
  <div class="body-text" style="left:111px;top:208px;font-weight:600">
    <div style="font-size:13px;line-height:1.15;font-weight:700">Was ist für Sie<br>wichtiger?</div>
    <div style="margin-top:12px;line-height:1.55">A) Zeitersparnis<br>B) Hygiene<br>C) Umweltfreundlichkeit<br><b>Kommentieren Sie!</b></div>
  </div>
</section>

<!-- 13 Lizenz -->
<section class="poster">
  <svg class="shapes" viewBox="0 0 314 395">
    <use href="#header" fill="var(--blue)"/>
    <path d="M95,380 C80,360 75,330 78,300 C85,220 160,185 240,188 C300,190 330,215 340,230 V360 C300,385 230,392 170,380 C140,395 105,400 80,398Z" fill="var(--white)" stroke="var(--blue-soft)" stroke-width="3"/>
  </svg>
  <div class="brand"><span class="brand-mark"></span><span class="brand-name">Wohnglanz<br>Pilot</span></div>
  <div class="title">REINIGUNGS<br>SERVICE</div>
  <div class="pill" style="left:60px;top:100px;width:250px;height:82px"></div>
  <div class="pill-text" style="left:108px;top:117px;font-size:11.5px;font-style:normal;font-weight:500;line-height:1.12">Werde <b style="font-weight:800;font-style:italic">Lizenznehmer</b> –<br>Starte dein <b style="font-weight:800">eigenes</b><br><b style="font-weight:800">Business</b> mit erprobtem<br>Konzept</div>
  <div class="quote" style="left:10px;top:120px">”</div>
  <div class="side" style="left:11px;top:178px;font-style:normal;font-weight:500;font-size:9px">Jetzt infor-<br>mieren &amp;<br>Teil unseres<br>Lizenz-<br>systems<br>werden!</div>
  <div class="body-text" style="left:80px;top:200px;width:225px;text-align:center;font-size:9.5px;line-height:1.45">
    <div><span>●</span> Du möchtest<br>dich selbstständig machen,<br>aber nicht bei Null anfangen?</div>
    <div style="margin-top:4px"><span>●</span> Profitiere von unserem bewährten<br>Geschäftsmodell</div>
    <div style="margin-top:4px"><span>●</span> Schulung &amp; laufende Unterstützung</div>
    <div style="margin-top:4px"><span>●</span> Volle unternehmerische Frei-<br>heit mit starkem Netzwerk</div>
  </div>
</section>

<!-- 14 Neuanfang -->
<section class="poster">
  <svg class="shapes" viewBox="0 0 314 395">
    <use href="#header" fill="var(--blue)"/>
    <path d="M0,330 C90,322 200,320 314,300 V395 H0Z" fill="var(--blue)"/>
    <path d="M95,325 C78,300 75,255 85,215 C100,160 170,150 240,155 C300,160 330,180 340,195 V310 C300,335 230,340 170,330 C140,340 110,340 95,325Z" fill="var(--white)" stroke="var(--blue-soft)" stroke-width="3"/>
    <use href="#spark" x="118" y="355" width="18" height="18" fill="var(--blue-soft)"/>
    <circle cx="142" cy="345" r="3" fill="var(--blue-soft)"/>
  </svg>
  <div class="brand"><span class="brand-mark"></span><span class="brand-name">Wohnglanz<br>Pilot</span></div>
  <div class="title">REINIGUNGS<br>SERVICE</div>
  <div class="photo" role="img" aria-label="Lächelnder Mann in hellem Hemd und Jeans zeigt Daumen hoch" style="left:12px;top:90px;width:82px;height:300px;border-radius:40px 40px 8px 8px;background:linear-gradient(180deg,#d9a98a 0%,#f0c9d2 25%,#e9b8c4 45%,#7e95b5 60%,#6c7fa0 95%)"></div>
  <div class="pill" style="left:90px;top:105px;width:220px;height:62px"></div>
  <div class="pill-text" style="left:110px;top:117px;font-size:15px">Zeit für deinen<br>Neuanfang!</div>
  <div class="quote" style="left:243px;top:175px;font-size:44px">”</div>
  <ul class="list body-text" style="left:98px;top:168px;font-size:9.5px;line-height:1.4">
    <li><span class="ring"></span><span>Du träumst davon, dein<br><b>eigener Chef</b><br>zu sein?</span></li>
    <li><span class="ring"></span><span>Wir suchen<br><b>engagierte Menschen</b> mit<br><b>Unternehmergeist!</b></span></li>
    <li><span class="ring"></span><span>Keine Erfahrung?<br>Kein Problem –<br>wir bringen dir alles bei.</span></li>
  </ul>
  <div class="foot" style="left:143px;top:352px;font-size:11px">Interessiert? schreib<br>uns einfach direkt!</div>
</section>

<!-- 15 Mehr als Lappen -->
<section class="poster">
  <svg class="shapes" viewBox="0 0 314 395">
    <use href="#header" fill="var(--blue)"/>
    <path d="M0,338 H314 V395 H0Z" fill="var(--blue)"/>
    <path d="M0,160 C30,140 100,145 120,175 V338 H0Z" fill="var(--blue-mid)"/>
    <g fill="none" stroke="var(--blue-deep)" stroke-width="1.2">
      <circle cx="138" cy="206" r="5"/>
      <circle cx="138" cy="230" r="6"/>
      <circle cx="138" cy="258" r="6"/>
      <circle cx="138" cy="285" r="6"/>
      <circle cx="138" cy="312" r="6"/>
    </g>
  </svg>
  <div class="brand"><span class="brand-mark"></span><span class="brand-name">Wohnglanz<br>Pilot</span></div>
  <div class="title">REINIGUNGS<br>SERVICE</div>
  <div class="pill" style="left:60px;top:100px;width:250px;height:70px"></div>
  <div class="pill-text" style="left:130px;top:112px;font-size:14px;font-style:normal;font-weight:500;line-height:1.1">Reinigung ist mehr<br>als nur den Lappen<br>schwingen!</div>
  <div class="a" style="left:20px;top:168px;color:var(--white);font-size:10.5px;line-height:1.2;font-weight:500">Reinigung ist<br>Handwerk,<br>Service und<br>Leidenschaft<br>in einem.</div>
  <div class="photo" role="img" aria-label="Lächelnde Reinigungskraft mit Staubwedel und Putzmitteln" style="left:2px;top:238px;width:120px;height:100px;border-radius:50% 50% 0 0;background:linear-gradient(180deg,#eef4f9 0%,#c98d6e 35%,#4fa4c9 70%,#e7c73a 100%)"></div>
  <div class="body-text" style="left:152px;top:201px;font-size:7.5px;line-height:1.25;color:var(--navy)">
    <div>Sorgfalt und Liebe zum Detail</div>
    <div style="margin-top:8px">Fachwissen über Materialien<br>und Reinigungstechniken</div>
    <div style="margin-top:7px">Verantwortung für Hygiene<br>und Gesundheit</div>
    <div style="margin-top:7px">Organisationstalent und<br>Verlässlichkeit</div>
    <div style="margin-top:7px">Kundenorientierung und<br>Vertrauen</div>
  </div>
  <div class="foot" style="left:11px;top:344px;font-size:7.5px;font-weight:500;line-height:1.4">Unsere ‘Wohnglanz Pilot’ sind echte Profis. die Räume nicht<br>nur sauber, sondern lebenswert machen.<br>Reinigung ist <b>Handwerk, Service und Leidenschaft</b> in einem.</div>
</section>

</main>
</body>
</html>
```